help us design packaging

Hello All, We have made our design guidelines much simpler and easier! Please see brief, give us something sexy!

Serif
Decorative
Script

```html
<!DOCTYPE html>
<html lang="en">
<head>
<meta charset="utf-8">
<title>Temperance Goods – Packaging</title>
<link rel="stylesheet" href="https://fonts.googleapis.com/css2?family=Oswald:wght@600&family=IM+Fell+English:ital@0;1&family=IM+Fell+English+SC&family=Tinos&display=swap">
<style>
  :root{
    --backdrop:#c3cfbd;
    --label-red:#dc6b68;
    --ink:#1c1a1a;
    --leaf-green:#3f8f2a;
    --vine-green:#4aa43a;
    --tin-silver:#dadada;
    --tin-silver-dark:#a9a9a9;
    --ring-black:#111111;
    --paper-white:#f4f1ea;
  }
  html,body{margin:0;padding:0;}
  body{
    width:1200px;height:586px;overflow:hidden;position:relative;
    background:var(--backdrop);
  }
  .piece{position:absolute;}
  .leaf-art{position:absolute;background:var(--leaf-green);border-radius:50% 50% 10% 10%;}

  /* Warning label */
  .warning-label{left:48px;top:4px;width:286px;height:160px;}
  .warning-label svg{position:absolute;inset:0;}
  .warning-title{position:absolute;top:15px;left:0;right:0;text-align:center;
    font-family:"Tinos",serif;font-size:14px;letter-spacing:1px;color:var(--ink);}
  .warning-cols{position:absolute;top:42px;left:46px;width:194px;display:flex;
    font-family:"Tinos",serif;font-size:11px;line-height:13px;color:var(--ink);}
  .warning-cols p{margin:0;flex:1;padding:0 3px;text-align:center;white-space:nowrap;}
  .warning-cols p + p{border-left:1px solid var(--ink);}
  .warning-ids{position:absolute;top:103px;left:78px;width:124px;padding:4px 4px;
    border:1px solid var(--ink);text-align:center;
    font-family:"Tinos",serif;font-size:9.5px;line-height:1.4;color:var(--ink);}

  /* Lids */
  .lid svg{display:block;}
  .lid-silver{left:90px;top:185px;}
  .lid-black{left:870px;top:175px;}
  .lid-brand{position:absolute;left:0;right:0;text-align:center;
    font-family:"IM Fell English SC",serif;line-height:1;}

  /* Front label */
  .front-label{left:800px;top:372px;width:370px;height:214px;}
  .front-label svg{position:absolute;left:25px;top:62px;}
  .ornament-art{position:absolute;left:110px;top:4px;width:150px;height:56px;
    background:linear-gradient(#1c1a1a 0 0) center/150px 3px no-repeat,
               radial-gradient(ellipse at 50% 70%,#1c1a1a 0 22%,transparent 23%);}
  .front-tagline{position:absolute;top:82px;left:0;right:0;text-align:center;
    font-family:"IM Fell English",serif;font-style:italic;font-size:14px;color:var(--ink);}
  .front-name{position:absolute;top:100px;left:0;right:0;text-align:center;
    font-family:"Oswald",sans-serif;font-weight:600;font-size:30px;letter-spacing:1px;color:var(--ink);}
  .front-foot{position:absolute;top:160px;left:0;right:0;text-align:center;
    font-family:"IM Fell English",serif;font-style:italic;font-size:10px;color:var(--ink);}
</style>
</head>
<body>

  <!-- Warning label -->
  <section class="piece warning-label">
    <svg width="286" height="160" viewBox="0 0 286 160" aria-hidden="true">
      <path d="M16 2 H270 A14 14 0 0 0 284 16 V144 A14 14 0 0 0 270 158 H16 A14 14 0 0 0 2 144 V16 A14 14 0 0 0 16 2Z"
            fill="var(--label-red)" stroke="var(--ink)" stroke-width="2.5"/>
      <path d="M22 10 H264 A12 12 0 0 0 276 22 V138 A12 12 0 0 0 264 150 H22 A12 12 0 0 0 10 138 V22 A12 12 0 0 0 22 10Z"
            fill="none" stroke="var(--ink)" stroke-width="1" stroke-dasharray="3 2"/>
      <path d="M34 50 q-14 30 0 60 M252 50 q14 30 0 60" fill="none" stroke="var(--ink)" stroke-width="1.5"/>
    </svg>
    <div class="warning-title">• WARNING •</div>
    <div class="warning-cols">
      <p>This product has<br>intoxicating effects<br>and may be habit<br>forming</p>
      <p>This product is<br>unlawful outside<br>Washington state</p>
    </div>
    <div class="warning-ids">WSLCB License # 500127<br>UBI # 600-418-252</div>
  </section>
  <div class="leaf-art" role="img" aria-label="Green leaf illustration" style="left:8px;top:100px;width:62px;height:68px;"></div>

  <!-- Silver lid -->
  <section class="piece lid lid-silver" style="width:340px;height:340px;">
    <svg width="340" height="340" viewBox="0 0 340 340" aria-hidden="true">
      <defs>
        <radialGradient id="silverFace" cx="45%" cy="40%" r="65%">
          <stop offset="0" stop-color="#ededed"/><stop offset="1" stop-color="var(--tin-silver-dark)"/>
        </radialGradient>
        <path id="silverTop" d="M42 170 A128 128 0 0 1 298 170"/>
        <path id="silverBottom" d="M30 170 A140 140 0 0 0 310 170"/>
      </defs>
      <circle cx="170" cy="170" r="168" fill="var(--tin-silver)" stroke="#8a8a8a" stroke-width="2"/>
      <circle cx="170" cy="170" r="158" fill="var(--ring-black)"/>
      <circle cx="170" cy="170" r="122" fill="url(#silverFace)" stroke="var(--paper-white)" stroke-width="2"/>
      <text font-family="IM Fell English SC, serif" font-size="19" fill="var(--paper-white)" text-anchor="middle">
        <textPath href="#silverTop" startOffset="50%">Greenleaf Blending Company</textPath>
      </text>
      <text font-family="IM Fell English SC, serif" font-size="19" fill="var(--paper-white)" text-anchor="middle">
        <textPath href="#silverBottom" startOffset="50%">Made in Washington, USA Est. 2014</textPath>
      </text>
    </svg>
    <div class="leaf-art" role="img" aria-label="Green leaf emblem" style="left:140px;top:68px;width:60px;height:54px;"></div>
    <div class="lid-brand" style="top:140px;font-size:34px;color:var(--ink);">Temperance<br>Goods</div>
    <div role="img" aria-label="Green vine flourish ornament" style="position:absolute;left:110px;top:222px;width:120px;height:40px;background:var(--vine-green);border-radius:50%;opacity:.85;"></div>
  </section>

  <!-- Black lid -->
  <section class="piece lid lid-black" style="width:190px;height:190px;">
    <svg width="190" height="190" viewBox="0 0 190 190" aria-hidden="true">
      <defs>
        <path id="blackTop" d="M24 95 A71 71 0 0 1 166 95"/>
        <path id="blackBottom" d="M18 95 A77 77 0 0 0 172 95"/>
      </defs>
      <circle cx="95" cy="95" r="93" fill="var(--ring-black)"/>
      <circle cx="95" cy="95" r="86" fill="none" stroke="var(--label-red)" stroke-width="1.5"/>
      <circle cx="95" cy="95" r="66" fill="none" stroke="var(--label-red)" stroke-width="1.5"/>
      <text font-family="IM Fell English SC, serif" font-size="11" fill="var(--label-red)" text-anchor="middle">
        <textPath href="#blackTop" startOffset="50%">Greenleaf Blending Company</textPath>
      </text>
      <text font-family="IM Fell English SC, serif" font-size="11" fill="var(--label-red)" text-anchor="middle">
        <textPath href="#blackBottom" startOffset="50%">Made in Washington, USA Est. 2014</textPath>
      </text>
    </svg>
    <div class="leaf-art" role="img" aria-label="Green leaf emblem" style="left:80px;top:34px;width:30px;height:28px;"></div>
    <div class="lid-brand" style="top:78px;font-size:19px;color:var(--label-red);">Temperance<br>Goods</div>
    <div role="img" aria-label="Green vine flourish ornament" style="position:absolute;left:68px;top:124px;width:54px;height:22px;background:var(--vine-green);border-radius:50%;"></div>
  </section>

  <!-- Front label -->
  <section class="piece front-label">
    <div class="ornament-art" role="img" aria-label="Black leaf and scroll ornament"></div>
    <svg width="320" height="130" viewBox="0 0 320 130" aria-hidden="true">
      <path d="M12 2 H308 A10 10 0 0 0 318 12 V118 A10 10 0 0 0 308 128 H12 A10 10 0 0 0 2 118 V12 A10 10 0 0 0 12 2Z"
            fill="var(--label-red)" stroke="var(--ink)" stroke-width="2.5"/>
      <path d="M16 9 H304 A7 7 0 0 0 311 16 V114 A7 7 0 0 0 304 121 H16 A7 7 0 0 0 9 114 V16 A7 7 0 0 0 16 9Z"
            fill="none" stroke="var(--ink)" stroke-width="1"/>
      <line x1="60" y1="80" x2="260" y2="80" stroke="var(--ink)" stroke-width="1.2"/>
    </svg>
    <div class="front-tagline">Finest Quality • Cured to Perfection</div>
    <div class="front-name">TEMPERANCE GOODS</div>
    <div class="front-foot">— World Famous —</div>
    <div class="leaf-art" role="img" aria-label="Green leaf illustration" style="left:0;top:150px;width:50px;height:64px;"></div>
    <div class="leaf-art" role="img" aria-label="Green leaf illustration" style="left:320px;top:150px;width:50px;height:64px;"></div>
  </section>

</body>
</html>
```